Website Design for Hulls for Heroes

Please design and code a new website.
Here are the sites I like best:
http://www.wavelarkit.com/alternate/
http://www.wheelsgivenback.org
Please make it similar. This is NOT a car donation site. It's a boat donation site. I just like this sites above as a lead generation sites.
Old site:
http://hullsforheroes.org
Updates
Coding
Coded - Design and coding required
Number of Pages Required
1 page
Look and feel
Each slider illustrates characteristics of the customer's brand and the style your logo design should communicate.

```html
<!DOCTYPE html>
<html lang="en">
<head>
<meta charset="utf-8">
<title>Hulls for Heroes – Donate your Boat</title>
<link rel="stylesheet" href="https://fonts.googleapis.com/css2?family=Raleway:wght@400;500;600;700;800&display=swap">
<style>
:root{
  --red:#c8141c;
  --red-dark:#a80d14;
  --blue:#3d5fd8;
  --blue-deep:#1f2fd0;
  --teal:#0f6b63;
  --link:#8ff5ec;
  --ink:#333;
  --muted:#888;
  --pale:#f4f4f4;
  --white:#fff;
  --overlay:rgba(30,30,30,.78);
}
*{box-sizing:border-box;margin:0;padding:0}
html,body{width:1200px;height:3600px;overflow:hidden;background:var(--white)}
body{position:relative;font-family:"Raleway",Arial,sans-serif;color:var(--ink)}
.abs{position:absolute}
.btn{position:absolute;background:var(--red);color:var(--white);font-size:13px;font-weight:500;display:flex;align-items:center;justify-content:center;gap:8px;border-radius:3px;white-space:nowrap}

/* hero */
.hero{left:84px;top:53px;width:1030px;height:720px;background:linear-gradient(180deg,#3c4a78 0%,#8a6a9c 30%,#e0a7a6 48%,#9b6a86 60%,#4b3c63 80%,#2b2a45 100%)}
.brand{left:82px;top:16px;display:flex;align-items:center;gap:8px;color:var(--white);font-weight:800;font-size:18px}
.brand i{width:14px;height:14px;background:var(--red);display:block}
.nav{right:252px;top:22px;display:flex;gap:22px;color:var(--white);font-size:11px;white-space:nowrap}
.nav-call{right:68px;top:16px;width:163px;height:26px;background:var(--red);color:var(--white);border-radius:13px;font-size:11px;display:flex;align-items:center;justify-content:center;white-space:nowrap}
.hero-pitch{left:40px;top:238px;width:560px;text-align:center;color:var(--white)}
.hero-pitch h2{font-size:26px;font-weight:700}
.hero-pitch .phone{font-size:52px;font-weight:700;color:var(--blue);line-height:1.1}
.hero-pitch p{font-size:14px}
.benefits{left:270px;top:390px;color:var(--white);font-size:12px;display:flex;align-items:center;gap:8px}
.form{left:600px;top:139px;width:353px;height:480px}
.form-head{height:156px;background:var(--red);padding:24px 20px;position:relative}
.form-head h3{color:var(--blue);font-size:28px;font-weight:700;line-height:1.15;width:270px}
.form-head p{color:var(--white);font-size:11px;margin-top:6px}
.form-head svg{position:absolute;right:18px;top:20px}
.form-body{height:324px;background:var(--teal);padding:20px 20px 0}
.field{height:19px;background:var(--white);margin-bottom:18px;font-size:10px;color:#999;padding:3px 8px;display:flex;justify-content:space-between}
.form-submit{height:38px;background:var(--red);color:var(--white);font-size:12px;display:flex;align-items:center;justify-content:center;margin-top:4px}

/* donate benefits */
.sec-title{left:0;width:1200px;text-align:center;color:var(--blue);font-weight:600;font-size:28px}
.rule{left:555px;width:90px;height:1px;background:#ddd}
.sub{left:0;width:1200px;text-align:center;color:var(--muted);font-size:14px}
.perk{width:150px;text-align:center;font-size:15px;color:#555;line-height:1.35}
.perk .dot{width:90px;height:90px;border-radius:50%;background:var(--pale);margin:0 auto 14px;display:flex;align-items:center;justify-content:center}
.perk .label{display:block;width:112px;margin:0 auto}

/* why */
.why{left:84px;top:1320px;width:1030px;height:475px;background:linear-gradient(180deg,#8aa4c2 0%,#6d8aa7 35%,#3f5d40 52%,#2f6aa0 70%,#1f5a8f 100%)}
.why-box{left:67px;top:38px;width:895px;height:286px;background:var(--overlay);padding:26px 70px}
.why-box h2{color:var(--white);text-align:center;font-size:28px;font-weight:600;margin-bottom:16px}
.why-row{display:flex;align-items:center;gap:16px;color:var(--white);font-size:12px;height:31px}
.why-row b{font-weight:700}
.arrow-dot{width:20px;height:20px;border-radius:50%;background:var(--red);display:flex;align-items:center;justify-content:center;flex:none}

/* how */
.how{left:84px;top:1795px;width:1030px;height:497px;background:var(--pale)}
.step{left:80px;width:520px}
.step .icon{position:absolute;left:0;top:0;width:44px;height:44px;border-radius:50%;background:var(--red);display:flex;align-items:center;justify-content:center}
.step h4{margin-left:66px;font-size:17px;font-weight:500;color:#444}
.step p{margin-left:66px;font-size:12px;color:var(--muted);margin-top:10px;line-height:1.6}

/* faq */
.faq{left:84px;top:2292px;width:1030px;height:439px;background:linear-gradient(180deg,#5f7890 0%,#8598ab 40%,#4b6277 70%,#2d3d4d 100%)}
.faq-box{left:118px;top:36px;width:794px;height:300px;background:var(--overlay);padding:14px 30px}
.faq-box h2{color:var(--white);text-align:center;font-size:28px;font-weight:600;margin-bottom:10px}
.faq-q{color:var(--red);font-size:12px;text-align:center;height:29px;display:flex;align-items:center;justify-content:center;border-bottom:1px solid rgba(255,255,255,.08);position:relative}
.faq-q::after{content:"";position:absolute;right:6px;width:7px;height:7px;border-right:2px solid var(--red);border-bottom:2px solid var(--red);transform:rotate(45deg)}

/* stats */
.stats{left:163px;top:2784px;font-weight:700;font-size:28px;line-height:1.3;color:var(--blue)}
.stats .deep{color:var(--blue-deep)}
.stats span{display:block}

/* footer */
.footer{left:84px;top:3187px;width:1030px;height:360px;background:linear-gradient(180deg,#e9e2d8 0%,#c4b7a7 45%,#6f6355 100%)}
.footer-box{left:67px;top:41px;width:895px;height:228px;background:rgba(40,40,40,.85);display:flex;padding:26px 36px;gap:40px;color:var(--white)}
.footer-box h5{font-size:16px;font-weight:500;margin-bottom:12px}
.about p{font-size:11px;line-height:1.75;color:#ddd;width:230px}
.badge-a{width:60px;height:30px;background:#c9c9c9;border-radius:4px;margin:12px 0 0 26px}
.badge-b{width:44px;height:44px;background:#cfe3f0;border-radius:50%;margin:26px 0 0 34px}
.call .num{color:var(--blue);font-size:28px;font-weight:700}
.call p{font-size:12px;color:#ddd}
.foot-bar{left:180px;top:312px;width:780px;display:flex;justify-content:space-between;color:var(--link);font-size:12px;font-weight:600;text-shadow:0 1px 2px rgba(0,0,0,.45)}
.foot-bar nav{display:flex;gap:22px}
</style>
</head>
<body>

<section class="abs hero" role="img" aria-label="Photo of a small boat on still water at sunset, reflected in the lake">
  <div class="abs brand"><i></i>Hulls for Heroes</div>
  <nav class="abs nav"><span>HOME</span><span>WHY Donate</span><span>KEY FEATURES</span><span>PROCESS</span><span>FAQ</span><span>ABOUT</span></nav>
  <div class="abs nav-call">CALL US 1-800-555-0142</div>

  <div class="abs hero-pitch">
    <h2>Call today to donate your Boat</h2>
    <div class="phone">1-800-555-0142</div>
    <p>Live Operators Available - 7 Days A Week</p>
  </div>
  <div class="abs benefits">Learn The benefits
    <svg width="12" height="14" viewBox="0 0 12 14"><path d="M6 1a4 4 0 0 1 4 4c0 3-4 8-4 8S2 8 2 5a4 4 0 0 1 4-4z" fill="none" stroke="#fff" stroke-width="1.4"/><circle cx="6" cy="5" r="1.3" fill="#fff"/></svg>
  </div>

  <form class="abs form">
    <div class="form-head">
      <h3>Donate your Boat online 24/7</h3>
      <p>Full Tax Deduction - Running or Not</p>
      <svg width="40" height="44" viewBox="0 0 40 44" fill="none" stroke="#3d5fd8" stroke-width="3"><circle cx="20" cy="6" r="4"/><path d="M20 10v30M10 18h20M4 26c0 9 8 14 16 14s16-5 16-14"/></svg>
    </div>
    <div class="form-body">
      <div class="field">First Name</div>
      <div class="field">Second Name</div>
      <div class="field">Email</div>
      <div class="field">Telefone Phone</div>
      <div class="field">Choose Year<span>▾</span></div>
      <div class="field">Choose Make<span>▾</span></div>
      <div class="field">Boat Model</div>
      <div class="form-submit">DONATE NOW</div>
    </div>
  </form>
</section>

<h2 class="abs sec-title" style="top:822px">Donate your Boat to veterans</h2>
<div class="abs rule" style="top:886px"></div>
<p class="abs sub" style="top:912px">Make a difference</p>

<div class="abs perk" style="left:151px;top:982px"><div class="dot"><svg width="36" height="36" viewBox="0 0 36 36" fill="#c8141c"><rect x="3" y="16" width="7" height="16"/><path d="M12 16l7-12c3 0 4 2 3 5l-1 5h9c2 0 3 2 2 4l-3 12c-1 2-2 2-4 2H12z"/></svg></div><span class="label">You have no costs</span></div>
<div class="abs perk" style="left:302px;top:982px"><div class="dot"><svg width="36" height="38" viewBox="0 0 40 44" fill="none" stroke="#c8141c" stroke-width="3.5"><circle cx="20" cy="6" r="4"/><path d="M20 10v30M10 18h20M4 26c0 9 8 14 16 14s16-5 16-14"/></svg></div><span class="label">Free towing, running or not</span></div>
<div class="abs perk" style="left:451px;top:982px"><div class="dot"><svg width="36" height="36" viewBox="0 0 36 36" fill="none" stroke="#c8141c" stroke-width="3"><path d="M26 20v10H6V10h12"/><path d="M14 22l2-6 12-12 4 4-12 12z"/></svg></div><span class="label">We issue you an IRS tax receipt</span></div>
<div class="abs perk" style="left:599px;top:982px"><div class="dot"><svg width="34" height="36" viewBox="0 0 34 36" fill="#c8141c"><path d="M4 2h14l6 6v6H14v20H4z"/><path d="M16 16h10l6 6v12H16z"/></svg></div><span class="label">We take Boate of all paperwork</span></div>
<div class="abs perk" style="left:748px;top:982px"><div class="dot"><svg width="34" height="38" viewBox="0 0 34 38" fill="none" stroke="#c8141c" stroke-width="3"><path d="M10 20L6 4M16 20l2-17M10 22h14c3 0 4 3 3 6l-3 6H12c-3 0-5-2-5-5z"/></svg></div><span class="label">No DMV Hassles</span></div>
<div class="abs perk" style="left:897px;top:982px"><div class="dot"><svg width="36" height="36" viewBox="0 0 36 36" fill="#c8141c"><path d="M20 2l14 14-18 18L2 20l4-4a3 3 0 0 0 4-4l4-4a3 3 0 0 0 4-4z"/></svg></div><span class="label">Vacation Voucher</span></div>

<div class="btn" style="left:532px;top:1218px;width:135px;height:38px">Donate your Boat ›</div>

<section class="abs why" role="img" aria-label="Photo of a speedboat cruising across open water with a treeline behind">
  <div class="abs why-box">
    <h2>Why donate your Boat to us</h2>
    <div class="why-row"><span class="arrow-dot"><svg width="10" height="10" viewBox="0 0 10 10"><path d="M1 5h7M5 2l3 3-3 3" stroke="#fff" stroke-width="1.6" fill="none"/></svg></span><span><b>IRS 501(c)3 Approved :</b> Free 24/7 Pickup with No DMV Hassles</span></div>
    <div class="why-row"><span class="arrow-dot"><svg width="10" height="10" viewBox="0 0 10 10"><path d="M1 5h7M5 2l3 3-3 3" stroke="#fff" stroke-width="1.6" fill="none"/></svg></span><span><b>Free Local Towing :</b> We will pick up your Boat donation, running or not, when it's most convenient, at home or work.</span></div>
    <div class="why-row"><span class="arrow-dot"><svg width="10" height="10" viewBox="0 0 10 10"><path d="M1 5h7M5 2l3 3-3 3" stroke="#fff" stroke-width="1.6" fill="none"/></svg></span><span><b>Income Tax Deduction :</b> We issue your IRS tax receipt and get you the highest tax write-off possible.</span></div>
    <div class="why-row"><span class="arrow-dot"><svg width="10" height="10" viewBox="0 0 10 10"><path d="M1 5h7M5 2l3 3-3 3" stroke="#fff" stroke-width="1.6" fill="none"/></svg></span><span><b>No Paperwork Hassles :</b> We handle everything DMV and IRS paperwork.</span></div>
    <div class="why-row"><span class="arrow-dot"><svg width="10" height="10" viewBox="0 0 10 10"><path d="M1 5h7M5 2l3 3-3 3" stroke="#fff" stroke-width="1.6" fill="none"/></svg></span><span><b>Schedule a Free Pickup :</b> Complete the form and a representative will call you to arrange a convenient time to pickup your Boat.</span></div>
  </div>
  <div class="btn" style="left:462px;top:376px;width:108px;height:38px">Donate Now ›</div>
</section>

<section class="abs how">
  <h2 class="abs sec-title" style="left:-84px;top:52px">How to donate your vehicle to veterans organization</h2>
  <div class="abs rule" style="left:471px;top:104px"></div>

  <div class="abs step" style="top:172px">
    <span class="icon"><svg width="20" height="20" viewBox="0 0 20 20"><path d="M5 2l3 4-2 2c1 3 3 5 6 6l2-2 4 3-2 3C9 18 2 11 2 4z" fill="#fff"/></svg></span>
    <h4>Call us at 1-888-555-0179 or Fill out the online form</h4>
    <p>Donating your vehicle is easy and donation is accepted nationwide.</p>
  </div>
  <div class="abs step" style="top:258px">
    <span class="icon"><svg width="20" height="20" viewBox="0 0 20 20" fill="#fff"><circle cx="10" cy="6" r="4"/><path d="M2 19c0-5 4-7 8-7s8 2 8 7z"/></svg></span>
    <h4>We tow the vehicle</h4>
    <p>Any vehicles are accepted and we will arrange to pick up your vehicle when<br>it is most convenient for you</p>
  </div>
  <div class="abs step" style="top:366px">
    <span class="icon"><svg width="20" height="20" viewBox="0 0 20 20" fill="#fff"><circle cx="10" cy="6" r="4"/><path d="M2 19c0-5 4-7 8-7s8 2 8 7z"/></svg></span>
    <h4>Tax write-off</h4>
    <p>Once the vehicle donation is complete, you will receive your tax deductable<br>vehicle donation receipt.</p>
  </div>

  <div class="abs" role="img" aria-label="Illustration of a white luxury motor yacht" style="left:612px;top:148px;width:290px;height:170px;background:radial-gradient(ellipse at 50% 60%,#ffffff 0%,#dfe6ee 45%,rgba(244,244,244,0) 75%)"></div>
</section>

<section class="abs faq" role="img" aria-label="Photo of a white and red boat with a canopy moored on a river">
  <div class="abs faq-box">
    <h2>Frequently asked questions</h2>
    <div class="faq-q">What kinds of boats can I donate?</div>
    <div class="faq-q">Does my boat need to be running to donate?</div>
    <div class="faq-q">Is there any cost for the pickup?</div>
    <div class="faq-q">How much can I deduct on my taxes?</div>
    <div class="faq-q">Do I need the title for my boat?</div>
    <div class="faq-q">How long does the pickup take?</div>
    <div class="faq-q">Where does my donation go?</div>
    <div class="faq-q">How do I donate a boat?</div>
  </div>
</section>

<div class="abs stats">
  <span>SINCE THE START OF</span>
  <span>THE AFGANISTAN and IRAQI</span>
  <span>WARS</span>
  <span>more than one million <span class="deep" style="display:inline">US MEN</span></span>
  <span class="deep">AND WOMEN</span>
  <span>have been <span class="deep" style="display:inline">WOUNDED or</span></span>
  <span class="deep">INJURED</span>
</div>
<div class="abs" role="img" aria-label="Illustration of a light blue cruise ship on waves" style="left:612px;top:2784px;width:348px;height:240px;background:radial-gradient(ellipse at 50% 55%,#c9e6f2 0%,#e6f3f9 45%,rgba(255,255,255,0) 72%)"></div>

<div class="btn" style="left:450px;top:3145px;width:300px;height:38px">donate your Boat and Express your Support ›</div>

<footer class="abs footer" role="img" aria-label="Faded photo of soldiers in silhouette with a flag">
  <div class="abs footer-box">
    <div class="about">
      <h5>About Valor Harbor Foundation</h5>
      <p>To serve veterans and their families with honor, dignity, and respect by advocating for and providing immediate assistance to them during times of crisis. Our country's warriors and heroes served bravely and faithfully. Valor Harbor is here during their time of need.</p>
    </div>
    <div class="secure" style="width:170px">
      <h5>Safe &amp; Secure</h5>
      <div class="badge-a"></div>
      <div class="badge-b"></div>
    </div>
    <div class="call">
      <h5>Call today to donate</h5>
      <div class="num">1-800-555-0142</div>
      <p>Live Operators Available - 7 Days A Week</p>
    </div>
  </div>
  <div class="abs foot-bar">
    <span>© All rights reserved</span>
    <nav><span>Top</span><span>WHY Donate</span><span>KEY FEATURES</span><span>PROCESS</span><span>FAQ</span><span>Terms</span></nav>
  </div>
</footer>

</body>
</html>
```